Global Consulting firm needs a Business Card Design (Contest)

We need a business card design for a company with global reach called 'MapleRidge Group'. MapleRidge Group is a Trusted Procurement Advisor that consults for Pinnacle 300 and Vantage 800 companies to find cost reductions in their spending. We would like to see designs that communicate fiduciary trust and sense of partnership. The Front should have our logo w/ 'trusted procurement advisor', Employee name and title, company address, email, phone and fax (logo attached "Maple ridge group final"). The color scheme and basic concept should be consistent with our presentation front page (attached "MRG presentation cover page"). The Back should have our website (www.mridgellc.com) and an array of our areas of expertise: office supplies, lab supplies, wireless telecom, MRO and IT (see "lab supplies" file for example).

```html
<!DOCTYPE html>
<html lang="en">
<head>
<meta charset="utf-8">
<title>MapleRidge Group – Business Card</title>
<link rel="stylesheet" href="https://fonts.googleapis.com/css2?family=Libre+Baskerville:ital,wght@0,400;0,700;1,400&family=Arimo:wght@400&display=swap">
<style>
  :root {
    --page-bg: #e4e2df;
    --card-bg: #ffffff;
    --ink: #141414;
    --brown: #9c4f22;
    --band: #121a16;
    --gold: #d8c41c;
    --tab-blue: #4b5fa6;
    --tab-edge: #2f3f7a;
    --map-tone: #e6d8d0;
    --logo-gold: #d9a520;
  }
  * { box-sizing: border-box; margin: 0; padding: 0; }
  html, body { width: 1200px; height: 1200px; overflow: hidden; }
  body {
    background: var(--page-bg);
    font-family: "Libre Baskerville", Georgia, serif;
    color: var(--ink);
    position: relative;
  }
  .card {
    position: absolute;
    width: 700px;
    height: 400px;
    background: var(--card-bg);
    overflow: hidden;
    box-shadow: 0 6px 18px rgba(0,0,0,.18);
  }
  .card--back { left: 250px; top: 120px; }
  .card--front { left: 250px; top: 660px; }

  /* Logo */
  .logo { position: absolute; display: flex; align-items: center; }
  .logo__dot {
    border-radius: 50%;
    background: var(--logo-gold);
    flex: none;
  }
  .logo__name { font-weight: 400; color: var(--ink); white-space: nowrap; }
  .tagline { position: absolute; font-style: italic; color: var(--ink); white-space: nowrap; }

  .card--back .logo { left: 48px; top: 52px; }
  .card--back .logo__dot { width: 58px; height: 58px; margin-right: 16px; }
  .card--back .logo__name { font-size: 42px; letter-spacing: -.5px; }
  .card--back .tagline { left: 160px; top: 118px; font-size: 24px; }

  .band {
    position: absolute; left: 0; top: 170px; width: 100%; height: 78px;
    background: var(--band);
  }
  .band__url {
    position: absolute; left: 0; right: 0; bottom: 12px;
    text-align: center; color: var(--gold);
    font-size: 17px; letter-spacing: 2.5px;
  }

  .expertise {
    position: absolute; left: 24px; top: 262px;
    display: flex; gap: 14px;
  }
  .expertise__tile {
    position: relative; width: 120px; height: 118px;
    border: 1.5px solid var(--tab-edge); border-radius: 6px;
    overflow: hidden; background: #f4f4f6;
  }
  .expertise__label {
    position: absolute; top: 0; left: 8px; right: 8px; height: 24px;
    background: var(--tab-blue); color: #fff;
    border-radius: 0 0 8px 8px;
    font-family: "Arimo", Arial, sans-serif; font-size: 13px;
    line-height: 24px; text-align: center; white-space: nowrap;
  }
  .expertise__image { position: absolute; left: 0; right: 0; top: 24px; bottom: 0; }
  .img--office { background: linear-gradient(135deg, #f6e27a, #f3a9c7 55%, #b9c8e8); }
  .img--lab { background: linear-gradient(135deg, #f4f4f6, #c9d8ef 50%, #e8b7cf); }
  .img--telecom { background: linear-gradient(135deg, #3a8fb4, #6fc7df 55%, #2a6f95); }
  .img--mro { background: linear-gradient(135deg, #f7f7f7, #c8c8cc 55%, #efefef); }
  .img--it { background: linear-gradient(135deg, #0f2f6e, #5fa4e8 55%, #12316a); }

  /* Front */
  .map {
    position: absolute; left: 30px; top: 118px; width: 540px; height: 270px;
    background: radial-gradient(ellipse at 55% 45%, var(--map-tone), rgba(230,216,208,.45) 70%, rgba(255,255,255,0));
  }
  .person__name {
    position: absolute; left: 260px; top: 52px;
    font-size: 48px; font-weight: 700; white-space: nowrap;
  }
  .person__title {
    position: absolute; left: 350px; top: 118px;
    font-size: 26px; color: var(--brown);
  }
  .rule {
    position: absolute; left: 0; top: 160px; width: 100%; height: 2px;
    background: var(--brown);
  }
  .card--front .logo { left: 360px; top: 210px; }
  .card--front .logo__dot { width: 38px; height: 38px; margin-right: 10px; }
  .card--front .logo__name { font-size: 27px; }
  .card--front .tagline { left: 410px; top: 254px; font-size: 16px; }

  .contact {
    position: absolute; left: 36px; top: 276px;
    list-style: none; font-size: 18px; letter-spacing: 1px; line-height: 30px;
  }
  .contact li, .address { display: flex; align-items: center; }
  .icon { width: 15px; height: 15px; margin-right: 12px; fill: var(--brown); flex: none; }
  .address {
    position: absolute; right: 34px; top: 296px;
    align-items: flex-start; font-size: 18px; letter-spacing: 1px; line-height: 30px;
  }
  .address .icon { margin-top: 7px; }
  .address__lines { text-align: right; }
</style>
</head>
<body>

<section class="card card--back">
  <div class="logo">
    <span class="logo__dot"></span>
    <span class="logo__name">MapleRidge Group</span>
  </div>
  <p class="tagline">Trusted Procurement Advisor</p>
  <div class="band"><p class="band__url">www.mridgellc.com</p></div>
  <div class="expertise">
    <div class="expertise__tile"><span class="expertise__label">Office Supplies</span><div class="expertise__image img--office" role="img" aria-label="Photo of colourful office supplies"></div></div>
    <div class="expertise__tile"><span class="expertise__label">Lap Supplies</span><div class="expertise__image img--lab" role="img" aria-label="Photo of laboratory supplies"></div></div>
    <div class="expertise__tile"><span class="expertise__label">Wireless Telecom</span><div class="expertise__image img--telecom" role="img" aria-label="Illustration of a wireless telecom network"></div></div>
    <div class="expertise__tile"><span class="expertise__label">MRO</span><div class="expertise__image img--mro" role="img" aria-label="Photo of a wrench and nut"></div></div>
    <div class="expertise__tile"><span class="expertise__label">IT</span><div class="expertise__image img--it" role="img" aria-label="Illustration of a glowing keyboard"></div></div>
  </div>
</section>

<section class="card card--front">
  <div class="map" role="img" aria-label="Faint world map in the background"></div>
  <h1 class="person__name">Daniel Hartley</h1>
  <p class="person__title">Director</p>
  <div class="rule"></div>
  <div class="logo">
    <span class="logo__dot"></span>
    <span class="logo__name">MapleRidge Group</span>
  </div>
  <p class="tagline">Trusted Procurement Advisor</p>

  <ul class="contact">
    <li><svg class="icon" viewBox="0 0 16 16"><path d="M3.5 1l3 3-1.6 2a9 9 0 0 0 5.1 5.1l2-1.6 3 3-2 2C7 14.5 1.5 9 1.5 3z"/></svg>(866) 555 – 0142</li>
    <li><svg class="icon" viewBox="0 0 16 16"><rect x="4" y="1" width="8" height="4"/><rect x="1" y="6" width="14" height="6" rx="1"/><rect x="4" y="10" width="8" height="5" fill="#fff" stroke="#9c4f22" stroke-width="1.5"/></svg>(609) 555 – 0188</li>
    <li><svg class="icon" viewBox="0 0 16 16"><rect x="1" y="3" width="14" height="10"/><path d="M1 3l7 6 7-6" fill="none" stroke="#fff" stroke-width="1.4"/></svg>info@mridgellc.com</li>
  </ul>

  <div class="address">
    <svg class="icon" viewBox="0 0 16 16"><path d="M8 0a5.5 5.5 0 0 0-5.5 5.5C2.5 10 8 16 8 16s5.5-6 5.5-10.5A5.5 5.5 0 0 0 8 0zm0 7.5a2 2 0 1 1 0-4 2 2 0 0 1 0 4z"/></svg>
    <div class="address__lines">4200 Harbor Crest Drive<br>Suite 310, Fairbrook<br>NJ 08099</div>
  </div>
</section>

</body>
</html>
```